Australian Meat, Seafood and Fresh Produce Website

Our organization is looking to design a simple, but eye catching website to show our services.
Our company exports West Australian FRESH fruit and vegetables, seafood and meat.
The website we are looking for would consist of:
- Landing Page
- Company info
- Directors bio
- Page that highlights our products
- Contact us page
We would like it to have a Chinese translated version as well.
Milo
Target Market(s)
Chinese Market
Industry/Entity Type
It Company
Number of Pages Required
1 page
Look and feel
Each slider illustrates characteristics of the customer's brand and the style your logo design should communicate.

```html
<!DOCTYPE html>
<html lang="en">
<head>
<meta charset="utf-8">
<title>Harbour Fresh Exports</title>
<link href="https://fonts.googleapis.com/css2?family=Lato:wght@400;700;900&display=swap" rel="stylesheet">
<style>
:root{
  --green:#7cc242;
  --ink:#222;
  --text:#666;
  --muted:#8a8a8a;
  --light:#efefef;
  --dark:#1e1e1e;
  --white:#fff;
}
*{box-sizing:border-box;margin:0;padding:0}
html,body{width:1200px;height:3504px;overflow:hidden;background:var(--white)}
body{font-family:'Lato',sans-serif;color:var(--text);position:relative}
section,header,footer{position:absolute;left:0;width:1200px}
.abs{position:absolute}
.center{text-align:center;left:0;width:1200px}
.btn{position:absolute;display:block;background:var(--green);color:var(--white);font-weight:700;font-size:13px;text-transform:uppercase;text-align:center;letter-spacing:.5px}
/* header */
.site-header{top:0;height:90px;background:var(--white)}
.brand{left:150px;top:26px;font-size:30px;font-weight:700;color:var(--ink);letter-spacing:-.5px;line-height:1.2}
.social-top{right:150px;top:12px;display:flex;gap:6px}
.social-top span{width:24px;height:24px;border-radius:50%;background:#9a9a9a}
.main-nav{right:150px;top:58px;display:flex;gap:24px;font-size:14px;font-weight:700;color:#333;text-transform:uppercase}
/* hero */
.hero{top:90px;height:576px;background:linear-gradient(180deg,#3b4756 0%,#2a3340 45%,#4a4a42 100%)}
.hero-title{top:218px;font-size:52px;line-height:1;font-weight:900;color:var(--white);white-space:nowrap}
.hero-title em{font-style:normal;color:var(--green)}
.hero-sub{top:282px;font-size:16px;color:#eee;line-height:1.5}
.hero-btn{position:absolute;left:495px;top:338px;width:210px;height:48px;border:2px solid var(--white);color:var(--white);font-size:14px;font-weight:700;line-height:44px;text-align:center;text-transform:uppercase}
/* section headings */
.sec-title{font-size:42px;line-height:1.1;font-weight:700;color:var(--ink);text-transform:uppercase}
.sec-sub{font-size:20px;line-height:1.3;color:var(--muted)}
.rule{width:60px;height:3px;background:var(--green);left:570px}
.small-para{font-size:13px;color:var(--muted);line-height:1.7;left:210px;width:780px;text-align:center}
/* about */
.about{top:666px;height:519px}
.about-kicker{left:150px;top:198px;font-size:13px;font-weight:900;color:var(--ink);text-transform:uppercase}
.about-text{left:150px;top:225px;width:480px;font-size:14px;line-height:1.65}
.about-photo{left:693px;top:159px;width:312px;height:312px;border-radius:50%;background:radial-gradient(circle,#c9d3dc 0%,#7f8e9b 60%,#4f5c68 100%)}
/* products */
.products{top:1185px;height:480px;background:var(--light)}
.card{top:159px;width:201px}
.card .pic{height:156px;position:relative}
.card .pic i{position:absolute;right:6px;bottom:6px;width:26px;height:26px;background:#444;border-radius:3px}
.card h4{margin-top:18px;font-size:20px;font-weight:700;color:var(--ink)}
.card p{margin-top:6px;font-size:12px;line-height:1.5;color:var(--muted)}
.card .btn{position:static;width:72px;height:24px;line-height:24px;font-size:11px;margin-top:16px}
/* gallery */
.gallery{top:1665px;height:780px}
.slider{top:237px;height:393px;background:linear-gradient(90deg,#6b3a28,#a8403a 30%,#c9605a 55%,#8c3a30 80%,#5a3022)}
.arrow{top:180px;width:40px;height:40px;border-radius:50%;border:2px solid var(--white)}
.thumbs{top:636px;display:flex;width:1200px;gap:2px}
.thumbs div{flex:1;height:144px}
/* team */
.team{top:2445px;height:594px}
.team .sec-title{text-transform:none}
.team-photo{left:150px;top:231px;width:456px;height:309px;background:linear-gradient(135deg,#111,#2b2b2b)}
.team-card{left:606px;top:231px;width:444px;height:309px;background:#e8e8e8;padding:9px}
.team-card .inner{position:relative;background:var(--white);width:100%;height:100%;text-align:center;padding:30px 36px 0}
.team-card h4{font-size:26px;font-weight:700;color:var(--ink);text-transform:uppercase}
.team-card p{margin-top:20px;font-size:13px;line-height:1.6;color:var(--muted)}
.team-card .btn{left:147px;top:234px;width:132px;height:36px;line-height:36px}
/* footer */
.map{top:3039px;height:336px;background:linear-gradient(180deg,#c9c7b8,#b3b0a0)}
.map::after{content:"";position:absolute;inset:0;background:rgba(30,30,30,.6)}
.signup{left:330px;top:93px;display:flex;z-index:1}
.signup .field{width:426px;height:48px;background:var(--white);font-size:14px;color:#555;padding:15px 14px}
.signup .go{width:114px;height:48px;background:var(--green);color:var(--white);font-size:13px;font-weight:700;line-height:48px;text-align:center;text-transform:uppercase}
.contact{top:162px;z-index:1;font-size:12px;color:#eee;line-height:1.6}
.social-foot{left:438px;top:246px;display:flex;gap:36px;z-index:1}
.social-foot span{width:42px;height:42px;border-radius:50%;border:2px solid #ddd}
.bottom{top:3375px;height:129px;background:var(--dark);color:#bbb}
.totop{top:24px;font-size:13px;color:var(--white)}
.foot-nav{top:54px;font-size:12px}
.foot-nav span{margin:0 10px}
.foot-nav .on{color:var(--white);font-weight:700;border-bottom:1px solid var(--white)}
.copy{top:100px;font-size:11px;color:#999}
</style>
</head>
<body>

<header class="site-header">
  <div class="abs brand">Harbour Fresh Exports</div>
  <div class="abs social-top"><span></span><span></span><span></span></div>
  <nav class="abs main-nav"><span>Home</span><span>About Us</span><span>Services</span><span>Directors Bio</span><span>Products</span><span>Contact Us</span></nav>
</header>

<section class="hero" role="img" aria-label="Loading dock with a refrigerated truck being filled with crates of fresh produce">
  <h1 class="abs center hero-title">WELCOME TO <em>HARBOUR FRESH EXPORTS</em></h1>
  <p class="abs center hero-sub">Lorem ipsum dolor sit amet, consectetur adipiscing elit, sed do eiusmod tempor incididunt ut labore<br>r adipiscing elit, sed do eiusmod tempor incididun</p>
  <div class="hero-btn">Know more about us</div>
</section>

<section class="about">
  <h2 class="abs center sec-title" style="top:38px">About Us</h2>
  <p class="abs center sec-sub" style="top:86px">An adventure in freshly foraged produce with rustic flavour &amp; charm</p>
  <div class="abs rule" style="top:124px"></div>
  <h3 class="abs about-kicker">Brand new home on the web</h3>
  <p class="abs about-text">Harbour Fresh Exports (HFE) aims to supply high quality West Australian produce to the rest of the world. Our state is known for its clean farming practices and environment, which produce meat, seafood, fruit and vegetables of a calibre that is respected globally.<br>With a management team and first class suppliers our organisation is able to provide quality ingredients, straight from farm or ocean to purchaser, in a timely manner to the highest quality.<br>This document aims to outline our management team and their backgrounds, as well as the suppliers who will supply our global customers.</p>
  <div class="btn" style="left:150px;top:456px;width:132px;height:36px;line-height:36px">Know more</div>
  <div class="abs about-photo" role="img" aria-label="Workers in white coats sorting seafood in a processing hall"></div>
</section>

<section class="products">
  <h2 class="abs center sec-title" style="top:34px">Our Products</h2>
  <p class="abs center sec-sub" style="top:86px;font-size:17px">Our menu and pricing do change from time to time, you will find the most current and accurate one.</p>
  <div class="abs rule" style="top:120px"></div>
  <div class="abs card" style="left:150px"><div class="pic" role="img" aria-label="Fresh fish and prawns on ice" style="background:linear-gradient(135deg,#9fb4c4,#c66a55 70%,#e2d6cc)"><i></i></div><h4>Fresh Sea Food</h4><p>Lorem ipsum dolor sit amet, consect etur adipiscing elit.</p><span class="btn">Read more</span></div>
  <div class="abs card" style="left:381px"><div class="pic" role="img" aria-label="Basket of mixed fresh vegetables" style="background:linear-gradient(135deg,#5b8a2e,#c7372c 55%,#e3a23a)"><i></i></div><h4>Fresh vegetables</h4><p>Lorem ipsum dolor sit amet, consect etur adipiscing elit.</p><span class="btn">Read more</span></div>
  <div class="abs card" style="left:615px"><div class="pic" role="img" aria-label="Crate of ripe oranges" style="background:linear-gradient(135deg,#e89a2a,#d9771d 60%,#8a4a1e)"><i></i></div><h4>Fresh Fruits</h4><p>Lorem ipsum dolor sit amet, consect etur adipiscing elit.</p><span class="btn">Read more</span></div>
  <div class="abs card" style="left:849px"><div class="pic" role="img" aria-label="Cuts of raw red meat" style="background:linear-gradient(135deg,#e6c3bd,#b8454a 60%,#7a2a2e)"><i></i></div><h4>Fresh Meat</h4><p>Lorem ipsum dolor sit amet, consect etur adipiscing elit.</p><span class="btn">Read more</span></div>
</section>

<section class="gallery">
  <h2 class="abs center sec-title" style="top:46px">Our Gallery</h2>
  <p class="abs center sec-sub" style="top:96px;font-size:17px">Lorem ipsum dolor sit amet, consectetur adipiscing elit sed do eiusmod tempor incididunt ut labore</p>
  <div class="abs rule" style="top:136px"></div>
  <p class="abs small-para" style="top:164px">Sed ut perspiciatis unde omnis iste natus error sit voluptatem accusantium doloremque laudantium, totam rem aperiam, eaque ipsa quae ab illo inventore veritatis et quasi architecto beatae vitae dicta sunt explicabo.</p>
  <div class="abs slider" style="left:0;width:1200px" role="img" aria-label="Racks of raw lamb cutlets on a wooden board">
    <svg class="abs arrow" style="left:150px" viewBox="0 0 40 40"><path d="M23 13l-7 7 7 7" fill="none" stroke="#fff" stroke-width="2.5"/></svg>
    <svg class="abs arrow" style="left:1008px" viewBox="0 0 40 40"><path d="M17 13l7 7-7 7" fill="none" stroke="#fff" stroke-width="2.5"/></svg>
  </div>
  <div class="abs thumbs">
    <div role="img" aria-label="Fresh fish on display" style="background:linear-gradient(135deg,#6d7a84,#b6c0c6)"></div>
    <div role="img" aria-label="Basket of vegetables" style="background:linear-gradient(135deg,#7a9a3a,#c0392b)"></div>
    <div role="img" aria-label="Limes and mandarins" style="background:linear-gradient(135deg,#9bbf3a,#e7a12c)"></div>
    <div role="img" aria-label="Cooked crayfish" style="background:linear-gradient(135deg,#c43a1f,#7a2a1a)"></div>
    <div role="img" aria-label="Packaged steak on a tray" style="background:linear-gradient(135deg,#2a2a2a,#b8464c)"></div>
    <div role="img" aria-label="Pile of yellow mangoes" style="background:linear-gradient(135deg,#f2c12e,#d9901e)"></div>
  </div>
</section>

<section class="team">
  <h2 class="abs center sec-title" style="top:46px">The Management Team</h2>
  <p class="abs center sec-sub" style="top:96px;font-size:17px">Lorem ipsum dolor sit amet, consectetur adipiscing elit eiusmod tempor incididunt ut labore</p>
  <div class="abs rule" style="top:136px"></div>
  <p class="abs small-para" style="top:164px">Sed ut perspiciatis unde omnis iste natus error sit voluptatem accusantium doloremque laudantium, totam rem aperiam, eaque ipsa quae ab illo inventore veritatis et quasi architecto beatae vitae dicta sunt explicabo.</p>
  <div class="abs team-photo" role="img" aria-label="Portrait of the managing director"></div>
  <div class="abs team-card"><div class="inner">
    <h4>Owen Hartley</h4>
    <p>Owen brings with him decades of experience in hospitality management, specialising in remote service and major site catering. Whilst managing remote sites across Australia and off shore rigs, Owen's management skills bring together supplier and logistical coordination to ensure the best outcomes for his clients.</p>
    <span class="btn">View more</span>
  </div></div>
</section>

<footer class="map" role="img" aria-label="Street map of the company location">
  <div class="abs signup"><div class="field">Enter your email address</div><div class="go">Subscribe</div></div>
  <p class="abs center contact">sales@harbourfresh.test - info@harbourfresh.test<br>lorem ipsum is dummy text</p>
  <div class="abs social-foot"><span></span><span></span><span></span><span></span><span></span></div>
</footer>

<footer class="bottom">
  <p class="abs center totop">&#9650; Back to Top</p>
  <p class="abs center foot-nav"><span class="on">Home</span><span>About Us</span><span>Directors Bio</span><span>Our Products</span><span>Gallery</span><span>Social</span><span>Contact</span></p>
  <p class="abs center copy">&copy; Copyright 2015. All Rights Reserved</p>
</footer>

</body>
</html>
```